Fall NHTA Postcard Design

I own Pinegrove Tumbling Athletic Club. We offer gymnastics classes to children ages 18vmonth to 18 years. We have a competitive team, an after school program and many day camps along with added on workshops. We will be offering two work shops this fall: Spanish Gymnastics... A class taught all in Spanish. Our second work shop will be Hip Hop Gymnastics.

I need a card that lets people know we are MORE than just gymnastics. We offer active options for children after school every day of the week and we are affordable. I want the front to be bright, fun and colorful and the back to have the schedule of classes we offer. I would like the front to drive people to our website: www.nhtwa.com or e-mail: info@nhtwa.com
I would like to front to offer a "Free Trial Class" *The details will be they can try it risk free, if they sign up then they pay for it as their start date. If not, no charge. Also, our after school program, sign up for 4 days get the 5th FREE! *For those who sign up for a month at a time. I have also added pictures of the gym. They are not necessary to have on the card, but put there as an option.

Our listed Mission Statement:
NHTA is dedicated to keeping kids moving! We are focused on allowing kids of all ages to be active and to have fun doing it. We encourage our students to learn gymnastics safely, while increasing self-confidence, body awareness, coordination, and skill. Children of all ages will build strength, increase flexibility, agility, balance and mental focus, while also learning how to incorporate overall fitness into a healthy lifestyle for years to come. We want to appropriately challenge each student and help them meet personal goals, while maintaining a happy and healthy environment for all.

Requirements
Must have
• Our gym Logo which is attached as the "NHTA Letter head" file.
Our contact info: www.nhtwa.com ~ Info@nhtwa.com ~ (802) 555-0147
Our class schedule on the back.
After School Program Begins: August 26th
Classes start: September 8th
"Stars" or "Bursts" on the Front with the "Free" listed on them, with an asterisk with it for the details on the back that really let you see the FREE
Must fit for a "over-sized card" looking to do 8.52"x5.47" size card
Nice to have
• A fun background picture on the front. It could be my gym or just fun bright with a "kid" having fun on it, upside down or whatever. I do not want "cluttered".
My gym colors are Black, Red and Gold but not necessary to use that color scheme.

```html
<!DOCTYPE html>
<html lang="en">
<head>
<meta charset="utf-8">
<title>Pinegrove Tumbling Athletic Club – Fall Postcard</title>
<link rel="stylesheet" href="https://fonts.googleapis.com/css2?family=Arvo:ital,wght@1,700&family=Open+Sans:wght@400;600;700;800&family=PT+Sans+Narrow:wght@400;700&family=PT+Sans:ital,wght@0,700;1,700&display=swap">
<style>
  :root{
    --backdrop:#e4e4e4;
    --ink:#1c1c1c;
    --charcoal:#2b2b2b;
    --charcoal-deep:#161616;
    --red:#c8141c;
    --red-deep:#8f0c12;
    --gold:#e0a81e;
    --gold-deep:#b8860b;
    --white:#ffffff;
    --silver:#e9e9e9;
  }
  *{box-sizing:border-box;margin:0;padding:0}
  html,body{width:1200px;height:1000px;overflow:hidden}
  body{background:var(--backdrop);position:relative;font-family:"Open Sans",sans-serif}

  /* ---------- Front ---------- */
  .card-front{position:absolute;left:62px;top:25px;width:711px;height:462px;background:var(--white);overflow:hidden}
  .front-shape{position:absolute;inset:0}
  .club-title{position:absolute;left:50px;top:22px;font-weight:800;font-size:19.5px;letter-spacing:3.2px;color:var(--ink)}
  .headline{position:absolute;font-family:"Arvo",serif;font-style:italic;font-weight:700;color:var(--red);transform:rotate(-5deg);transform-origin:left bottom;line-height:1}
  .headline-top{left:60px;top:58px;font-size:46px}
  .headline-main{left:66px;top:95px;font-size:86px;letter-spacing:-1px;text-shadow:0 2px 0 var(--red-deep)}
  .dates{position:absolute;right:58px;top:188px;text-align:center;color:var(--gold);font-weight:700;font-size:16px;letter-spacing:.6px;line-height:32px}
  .offer-band{position:absolute;left:0;top:253px;width:446px;height:139px;background:linear-gradient(90deg,var(--red-deep),var(--red) 45%,#d7222a)}
  .offer-list{position:absolute;left:200px;top:12px;list-style:none;font-family:"PT Sans",sans-serif;font-style:italic;font-weight:700;font-size:19px;line-height:24px;color:var(--white)}
  .offer-list li{margin-bottom:6px}
  .offer-list sup{font-size:11px;color:#f3b6b6}
  .offer-note{position:absolute;left:20px;bottom:9px;font-family:"PT Sans",sans-serif;font-style:italic;font-weight:700;font-size:9px;color:var(--white)}
  .free-badge{position:absolute;left:48px;top:244px;width:134px;height:134px}
  .gym-photo{position:absolute;left:446px;top:253px;width:265px;height:139px;background:linear-gradient(180deg,#c9c6c0 0%,#8e8a86 30%,#3a5fa8 55%,#2a4a8f 80%,#c43b2c 100%)}
  .front-contact{position:absolute;left:0;right:0;top:406px;text-align:center;color:var(--gold);font-weight:600;font-size:19px;letter-spacing:1.2px}

  /* ---------- Back ---------- */
  .card-back{position:absolute;left:418px;top:507px;width:703px;height:461px;background:var(--white);overflow:hidden}
  .schedule-panel{position:absolute;left:0;top:0;width:299px;height:461px;background:radial-gradient(ellipse at 50% 40%,#3a3a3a,var(--charcoal-deep) 85%)}
  .name-plate{position:absolute;left:24px;top:21px;width:248px;height:104px;border-radius:9px;background:linear-gradient(180deg,#fafafa,#cfcfcf 55%,#f2f2f2);display:flex;align-items:center;justify-content:center;text-align:center}
  .name-plate span{font-family:"Arvo",serif;font-style:italic;font-weight:700;font-size:17px;line-height:22px;color:var(--ink)}
  .schedule-col{position:absolute;top:138px;width:140px;font-family:"PT Sans Narrow",sans-serif}
  .col-left{left:26px}.col-right{left:176px}
  .class-name{color:var(--gold);font-weight:700;font-size:9.5px;text-transform:uppercase;margin-top:12px;line-height:12px}
  .class-name:first-child{margin-top:0}
  .class-times{list-style:none;color:var(--white);font-size:8.5px;line-height:12.6px;text-transform:uppercase}
  .class-times li::before{content:"• "}
  .address{position:absolute;left:308px;top:24px;font-size:10px;line-height:13px;color:var(--charcoal)}
  .address .phone{display:block;color:var(--red);font-weight:700;font-size:13px;margin-top:9px;line-height:16px}
  .address .web{display:block;font-size:9px;font-weight:600;margin-top:2px}
  .stamp-box{position:absolute;left:599px;top:11px;width:103px;height:103px;border:1px solid #e2e2e2}
  .workshop-box{position:absolute;left:299px;top:203px;width:174px;height:218px;background:linear-gradient(180deg,var(--red),var(--red-deep));color:var(--white);text-align:center;font-family:"PT Sans Narrow",sans-serif;font-weight:700}
  .ws-title{font-size:27px;line-height:26px;margin-top:30px}
  .ws-title sup{font-size:15px}
  .ws-time{font-size:13px;margin-top:3px}
  .ws-note{font-family:"PT Sans",sans-serif;font-style:italic;font-weight:400;font-size:7.2px;line-height:9.5px;margin:18px 10px 0}
  .workshop-badge{position:absolute;left:280px;top:122px;width:100px;height:100px}
</style>
</head>
<body>

<section class="card-front">
  <svg class="front-shape" width="711" height="462" viewBox="0 0 711 462" aria-hidden="true">
    <defs>
      <linearGradient id="darkFade" x1="0" y1="0" x2="0" y2="1">
        <stop offset="0" stop-color="#3a3a3a"/><stop offset="1" stop-color="#1a1a1a"/>
      </linearGradient>
    </defs>
    <path d="M0,95 C25,150 80,178 190,172 L470,150 C610,140 690,80 711,0 V462 H0 Z" fill="url(#darkFade)"/>
  </svg>

  <div class="club-title">PINEGROVE TUMBLING ATHLETIC CLUB</div>
  <div class="headline headline-top">Keeping</div>
  <div class="headline headline-main">Kids Moving!</div>

  <div class="dates">
    <p>AFTER SCHOOL MINI CAMP STARTS AUGUST 26TH</p>
    <p>CLASSES START ON SEPTEMBER 8TH</p>
  </div>

  <div class="offer-band">
    <ul class="offer-list">
      <li>• Free Trial Class<sup>*</sup></li>
      <li>• After school program<br>&nbsp;&nbsp;sign up for 4 days get<br>&nbsp;&nbsp;the 5th Free<sup>**</sup></li>
    </ul>
    <p class="offer-note">*Try it risk free, sign up and start pay that date. If not, no charge. **If sign up for a month at a time.</p>
  </div>

  <svg class="free-badge" viewBox="0 0 134 134" aria-hidden="true">
    <defs>
      <radialGradient id="goldFill" cx="0.4" cy="0.35" r="0.7">
        <stop offset="0" stop-color="#f2c54a"/><stop offset="1" stop-color="#b8860b"/>
      </radialGradient>
    </defs>
    <path d="M67,8 A58,58 0 1 1 30,112 L10,128 L20,100 A58,58 0 0 1 67,8 Z" fill="#ffffff"/>
    <circle cx="67" cy="66" r="50" fill="url(#goldFill)"/>
    <text x="67" y="78" text-anchor="middle" transform="rotate(-14 67 66)" font-family="Open Sans, sans-serif" font-weight="800" font-size="32" fill="#ffffff">FREE!</text>
  </svg>

  <div class="gym-photo" role="img" aria-label="Photo of the gym floor with colourful mats, an inflatable slide and training equipment"></div>

  <p class="front-contact">(802) 555-0147 • WWW.NHTWA.COM • INFO@NHTWA.COM</p>
</section>

<section class="card-back">
  <div class="schedule-panel">
    <div class="name-plate"><span>PINEGROVE TUMBLING<br>ATHLETIC CLUB</span></div>

    <div class="schedule-col col-left">
      <h3 class="class-name">Mom, Pop &amp; Tot</h3>
      <ul class="class-times"><li>Wednesday• Tuesday 5:00 - 5:45</li><li>Thursday 11 - 11:45</li><li>Saturday 9:00 - 9:45</li></ul>
      <h3 class="class-name">Pre-K</h3>
      <ul class="class-times"><li>Tuesday 4-4:50, 5-5:50, 5:50-6:40</li><li>Thursday 10:05-10:55</li><li>Saturday 10:00-10:50</li></ul>
      <h3 class="class-name">Kindergym</h3>
      <ul class="class-times"><li>Tuesday 3:15-4:05, 5-5:50, 5:50-6:40</li><li>Saturday 10:00-10:50</li></ul>
      <h3 class="class-name">Beginner I</h3>
      <ul class="class-times"><li>Monday 3:15-4:15, 4:15-5:15, 5:15-6:15</li><li>Thursday 4:00-5:00</li><li>Saturday 11:00-12:00</li></ul>
      <h3 class="class-name">Beginner II</h3>
      <ul class="class-times"><li>Monday 5:15-6:30</li><li>Wednesday 3:15-4:30</li><li>Thursday 5:00-6:15</li><li>Saturday 11:00-12:15</li></ul>
    </div>

    <div class="schedule-col col-right">
      <h3 class="class-name">Int./Adv</h3>
      <ul class="class-times"><li>Thursday 5:00-6:30</li><li>Friday 4:30-6:00</li><li>Saturday 11:00-12:30</li></ul>
      <h3 class="class-name">Boys 6 &amp; Up</h3>
      <ul class="class-times"><li>Wednesday 4:30-5:30, 5:30-6:30</li></ul>
      <h3 class="class-name">Boys Team All Ages</h3>
      <ul class="class-times"><li>Wednesday 4:30-6:30</li></ul>
      <h3 class="class-name">Parent &amp; Tot Open Gym</h3>
      <ul class="class-times"><li>Monday 10-11:30</li><li>Friday 10-11:30</li></ul>
      <h3 class="class-name">PVSD Early Rel. Camp</h3>
      <ul class="class-times"><li>Wednesday 12:30-5:00</li></ul>
      <h3 class="class-name">After School Camp</h3>
      <ul class="class-times"><li>Monday to Friday 3:00-5:00</li></ul>
      <h3 class="class-name">Birthday Parties</h3>
      <ul class="class-times"><li>Saturday 4:00-5:30, 6:00-7:30</li><li>Sunday 3:00-4:30</li></ul>
    </div>
  </div>

  <address class="address">
    42 Maple Ridge Road<br>Pinegrove,<br>Vermont,&nbsp; 05999
    <span class="phone">(802) 555-0147</span>
    <span class="web">www.nhtwa.com • Info@nhtwa.com</span>
  </address>

  <div class="stamp-box"></div>

  <div class="workshop-box">
    <p class="ws-title">SPANISH<br>GYM W.S.<sup>*</sup></p>
    <p class="ws-time">THURSDAY 9:15-10:00</p>
    <p class="ws-title" style="margin-top:14px">HIP HOP GYM<sup>*</sup></p>
    <p class="ws-time">FRIDAY 3:30-4:30</p>
    <p class="ws-note">* Will Run 4 weeks at a time as a work shop. Priced differently then regular running classes. Will change classes offered throughout the year.</p>
  </div>

  <svg class="workshop-badge" viewBox="0 0 100 100" aria-hidden="true">
    <defs>
      <radialGradient id="goldFill2" cx="0.4" cy="0.35" r="0.7">
        <stop offset="0" stop-color="#f2c54a"/><stop offset="1" stop-color="#b8860b"/>
      </radialGradient>
    </defs>
    <path d="M47,3 A44,44 0 1 1 78,78 L92,96 L66,88 A44,44 0 0 1 47,3 Z" fill="#ffffff"/>
    <circle cx="47" cy="46" r="38" fill="url(#goldFill2)"/>
    <g transform="rotate(-12 47 46)" font-family="Open Sans, sans-serif" font-weight="800" font-size="19" fill="#ffffff" text-anchor="middle">
      <text x="47" y="43">WORK</text>
      <text x="47" y="63">SHOPS</text>
    </g>
  </svg>
</section>

</body>
</html>
```